Business card for Verano Living

Hi again, I need a business card for my Verano Living business you have been working on with the following information:

Clara Hollis
Director
m. 0412 736 258
e. clara@veranoliving-example.com.au
w. www.veranoliving-example.com.au

Maybe you could use the original design (using both the green & white) and where the white box is you could include the above details (name / mobile / etc) - Perhaps the 'i' in Clara could be the bow tie again?

Then the back could be green with black writing stating:

Services Offered:

* Personal Assistant Concierge
* Decluttering Concierge
* Home Management Concierge
* FIFO Concierge
* Events Concierge
* Leisure & Travel Concierge
* Seasonal Concierge
* Professional Concierge

Many thanks
Updates

Hi Everyone I'm really sorry but I am working with just one designer on this brief, thank you for your work and apologies for my error.

Industry/Entity Type

Business

```html
<!DOCTYPE html>
<html lang="en">
<head>
<meta charset="utf-8">
<title>Verano Living – Business Card Presentation</title>
<link rel="stylesheet" href="https://fonts.googleapis.com/css2?family=Open+Sans:wght@400;600;700&display=swap">
<style>
  :root {
    --sheet-centre: #ffffff;
    --sheet-edge: #e3e3e3;
    --card-white: #ffffff;
    --card-border: #dcdcdc;
    --brand-green: #84c225;
    --brand-red: #c8171e;
    --ink: #2b2b2b;
    --name-red: #c8171e;
    --on-colour: #ffffff;
  }
  * { box-sizing: border-box; margin: 0; padding: 0; }
  html, body { width: 1200px; height: 849px; overflow: hidden; }
  body {
    position: relative;
    font-family: "Open Sans", sans-serif;
    background: radial-gradient(ellipse at 50% 50%, var(--sheet-centre) 0%, #f4f4f4 45%, var(--sheet-edge) 100%);
  }
  .card {
    position: absolute;
    width: 371px;
    height: 217px;
    border-radius: 11px;
    overflow: hidden;
  }
  .card--front {
    background: var(--card-white);
    border: 1px solid var(--card-border);
    box-shadow: 0 1px 3px rgba(0,0,0,0.06);
  }
  .card--back-green { background: var(--brand-green); }
  .card--back-red { background: var(--brand-red); }

  .row-top { top: 131px; }
  .row-bottom { top: 484px; }
  .col-left { left: 170px; }
  .col-right { left: 689px; }

  /* Front */
  .brand {
    position: absolute;
    left: 22px;
    top: 76px;
    width: 110px;
    display: flex;
    flex-direction: column;
    align-items: center;
    gap: 7px;
  }
  .brand__dot {
    width: 38px;
    height: 38px;
    border-radius: 50%;
    background: var(--brand-red);
  }
  .brand__name {
    font-size: 12.5px;
    font-weight: 700;
    color: var(--ink);
    white-space: nowrap;
    letter-spacing: -0.2px;
  }
  .contact {
    position: absolute;
    left: 160px;
    top: 74px;
    color: var(--ink);
    white-space: nowrap;
  }
  .contact__name,
  .contact__role {
    margin-left: 14px;
    font-size: 11.5px;
    line-height: 15px;
  }
  .contact__name { color: var(--name-red); }
  .contact__role { margin-bottom: 9px; }
  .contact__line {
    display: flex;
    align-items: center;
    gap: 5px;
    height: 13.5px;
    font-size: 10px;
    line-height: 13.5px;
    letter-spacing: -0.05px;
  }
  .contact__icon { width: 9px; height: 10px; flex: none; }

  /* Back */
  .back__disc {
    position: absolute;
    left: 271px;
    top: -29px;
    width: 144px;
    height: 144px;
    border-radius: 50%;
    background: var(--card-white);
  }
  .services {
    position: absolute;
    left: 24px;
    top: 98px;
    color: var(--on-colour);
    white-space: nowrap;
  }
  .services__title {
    font-size: 15px;
    font-weight: 600;
    line-height: 1.2;
  }
  .services__rule {
    width: 165px;
    height: 1px;
    margin: 5px 0 6px;
    background: linear-gradient(to right, rgba(255,255,255,0.9), rgba(255,255,255,0));
  }
  .services__list {
    list-style: none;
    font-size: 12.2px;
    line-height: 16.4px;
  }
</style>
</head>
<body>

  <!-- Green set: front -->
  <section class="card card--front row-top col-left">
    <div class="brand">
      <span class="brand__dot"></span>
      <span class="brand__name">Verano Living</span>
    </div>
    <div class="contact">
      <p class="contact__name">Clara Hollis</p>
      <p class="contact__role">Director</p>
      <p class="contact__line">
        <svg class="contact__icon" viewBox="0 0 9 10"><rect x="1.5" y="0.5" width="6" height="9" rx="1" fill="none" stroke="#2b2b2b" stroke-width="1"/><line x1="3.5" y1="8" x2="5.5" y2="8" stroke="#2b2b2b"/></svg>
        0412 736 258
      </p>
      <p class="contact__line">
        <svg class="contact__icon" viewBox="0 0 9 10"><rect x="0.5" y="2.5" width="8" height="6" fill="none" stroke="#2b2b2b" stroke-width="1"/><polyline points="0.5,2.5 4.5,6 8.5,2.5" fill="none" stroke="#2b2b2b" stroke-width="1"/></svg>
        clara@veranoliving-example.com.au
      </p>
      <p class="contact__line">
        <svg class="contact__icon" viewBox="0 0 9 10"><circle cx="4.5" cy="5" r="3.8" fill="none" stroke="#2b2b2b" stroke-width="1"/><line x1="0.7" y1="5" x2="8.3" y2="5" stroke="#2b2b2b" stroke-width="0.8"/></svg>
        www.veranoliving-example.com.au
      </p>
    </div>
  </section>

  <!-- Green set: back -->
  <section class="card card--back-green row-top col-right">
    <span class="back__disc"></span>
    <div class="services">
      <h2 class="services__title">Services Offered:</h2>
      <div class="services__rule"></div>
      <ul class="services__list">
        <li>Personal Assistant Concierge | Decluttering Concierge</li>
        <li>Home Management Concierge | FIFO Concierge</li>
        <li>Events Concierge | Leisure &amp; Travel Concierge</li>
        <li>Seasonal Concierge | Professional Concierge</li>
      </ul>
    </div>
  </section>

  <!-- Red set: front -->
  <section class="card card--front row-bottom col-left">
    <div class="brand">
      <span class="brand__dot"></span>
      <span class="brand__name">Verano Living</span>
    </div>
    <div class="contact">
      <p class="contact__name">Clara Hollis</p>
      <p class="contact__role">Director</p>
      <p class="contact__line">
        <svg class="contact__icon" viewBox="0 0 9 10"><rect x="1.5" y="0.5" width="6" height="9" rx="1" fill="none" stroke="#2b2b2b" stroke-width="1"/><line x1="3.5" y1="8" x2="5.5" y2="8" stroke="#2b2b2b"/></svg>
        0412 736 258
      </p>
      <p class="contact__line">
        <svg class="contact__icon" viewBox="0 0 9 10"><rect x="0.5" y="2.5" width="8" height="6" fill="none" stroke="#2b2b2b" stroke-width="1"/><polyline points="0.5,2.5 4.5,6 8.5,2.5" fill="none" stroke="#2b2b2b" stroke-width="1"/></svg>
        clara@veranoliving-example.com.au
      </p>
      <p class="contact__line">
        <svg class="contact__icon" viewBox="0 0 9 10"><circle cx="4.5" cy="5" r="3.8" fill="none" stroke="#2b2b2b" stroke-width="1"/><line x1="0.7" y1="5" x2="8.3" y2="5" stroke="#2b2b2b" stroke-width="0.8"/></svg>
        www.veranoliving-example.com.au
      </p>
    </div>
  </section>

  <!-- Red set: back -->
  <section class="card card--back-red row-bottom col-right">
    <span class="back__disc"></span>
    <div class="services">
      <h2 class="services__title">Services Offered:</h2>
      <div class="services__rule"></div>
      <ul class="services__list">
        <li>Personal Assistant Concierge | Decluttering Concierge</li>
        <li>Home Management Concierge | FIFO Concierge</li>
        <li>Events Concierge | Leisure &amp; Travel Concierge</li>
        <li>Seasonal Concierge | Professional Concierge</li>
      </ul>
    </div>
  </section>

</body>
</html>
```